Coupon/promo code site

I am looking for a one page website that will provide a list of coupon codes that are used at checkout when buying something online. The site will only have coupon codes for one online retailer. I would like this to be generic (i.e. not specific to any one retailer). I would like to have some interchangeable parts so that I could later customize the site so that it is specific to any given retailer.

I envision the site having a list of coupon codes with information about each code like when it expires and what it provides. For example there would be a: code, expiration date, short description or name, and a longer description (i.e. details).
Updates

Project Deadline Extended
Reason: I am going to submit a wire frame that provides a better idea of what I am looking for.

I have uploaded a wire frame that gives a more clear indication of what I am looking for.  Please see this before submitting designs.  If you have already submitted a design, please revise your design considering the wire frame I have provided.

Thanks,
Derek

Target Market(s)

Someone who is shopping online and searching for a specific retailers coupon codes

Industry/Entity Type

Coupon

Requirements
Must have
• I would like the site to have a white or light colored background.

I need a place or two where I can interchangeably place different retailers' logos.

The web page should have a title like, "[retailer's] online coupon code"

In addition to a list or table of coupon codes, there should below this be a list or table of special offers or sale items.

At the very bottom in a way that is not too noticeable, it should say, "This coupon site was created by PLW Deals."

There should be a section (probably on the right side) that allows a user to submit their email address to be notified in the future of specials/deals for this retailer.

There should be a nice looking link that goes to the online retailer's website.
Nice to have
• Example sites with a look and feel that I like are:

http://www.trolvania.com/
https://thebrimlet.com/
http://www.pixelgrove.com

This is an example of a site with coupon codes for just one retailer. This site is a little too busy, but you get the idea:
www.makeaplank.com/coupon-codes‎

```html
<!DOCTYPE html>
<html lang="en">
<head>
<meta charset="utf-8">
<title>Company Name Coupon Codes</title>
<link rel="stylesheet" href="https://fonts.googleapis.com/css2?family=Jost:wght@700&family=Noto+Sans:wght@400&family=Arimo:wght@400;700&family=Fjalla+One&display=swap">
<style>
:root{
  --blue:#0a7ab8;
  --bar-blue:#0590d0;
  --expiry:#e0262b;
  --panel:#e3e3e3;
  --ink:#333;
  --muted:#666;
  --code-dark:#555;
  --code-light:#8a8a8a;
  --hint:#ee1d23;
  --logo-block:#d6d6d6;
  --white:#fff;
  --rule:#cfcfcf;
}
*{box-sizing:border-box;margin:0;padding:0}
html,body{width:1143px;height:1200px;overflow:hidden;background:var(--white)}
body{position:relative;font-family:"Arimo",Arial,sans-serif;color:var(--ink)}
.abs{position:absolute}

.site-header{left:0;top:0;width:1143px;height:132px;border-bottom:1px dashed var(--rule)}
.brand-slot{left:23px;top:29px;width:258px;height:77px;background:var(--logo-block);border-radius:8px;display:flex;align-items:center;justify-content:center;gap:12px}
.brand-slot .mark{width:18px;height:18px;background:var(--muted)}
.brand-slot .name{font-family:"Arimo",Arial,sans-serif;font-weight:700;font-size:28px;color:var(--muted)}
.page-title{left:330px;top:36px;font-family:"Jost",sans-serif;font-weight:700;font-size:52px;color:var(--blue);white-space:nowrap}

.welcome{left:0;top:132px;width:1143px;height:208px;border-bottom:1px dashed var(--rule);text-align:center;padding-top:42px;font-family:"Noto Sans",sans-serif;font-weight:400;font-size:32px;line-height:43px;color:var(--ink)}

.coupon-panel{left:8px;top:358px;width:806px;height:682px;background:var(--panel);border-radius:18px}
.panel-bar{left:17px;top:367px;width:787px;height:47px;background:var(--bar-blue);border-radius:10px;display:flex;align-items:center;padding-left:20px;font-family:"Jost",sans-serif;font-weight:700;font-size:23px;color:var(--white)}
.panel-bar::after{content:"";position:absolute;inset:3px;border:1px dashed rgba(255,255,255,.9);border-radius:8px}

.coupon-card{left:20px;width:781px;height:140px;background:var(--white);border-radius:9px}
.coupon-card .offer{position:absolute;left:21px;top:14px;font-size:20px;font-weight:400;color:var(--ink)}
.coupon-card .details{position:absolute;left:21px;top:41px;width:400px;font-size:13px;line-height:16px;color:var(--ink)}
.coupon-card .code-label{position:absolute;left:482px;top:14px;font-size:20px;color:var(--ink)}
.coupon-card .code{position:absolute;left:626px;top:12px;width:139px;height:33px;border-radius:10px;background:var(--code-dark);color:var(--white);font-weight:700;font-size:16px;letter-spacing:1px;display:flex;align-items:center;justify-content:center}
.coupon-card .code.revealed{background:var(--code-light)}
.coupon-card .copy-hint{position:absolute;left:623px;top:52px;width:146px;height:45px;background:var(--hint);border-radius:8px;color:var(--white);font-size:13px;display:flex;align-items:center;justify-content:center}
.coupon-card .copy-hint::before{content:"";position:absolute;left:40px;top:-10px;border-left:12px solid transparent;border-bottom:12px solid var(--hint)}
.coupon-card .copy-hint b{font-weight:700;margin-right:4px}
.coupon-card .expires{position:absolute;left:21px;top:101px;font-size:16px;color:var(--expiry)}
.coupon-card .store{position:absolute;right:22px;top:102px;font-size:16px;color:var(--ink)}
.coupon-card .store strong{margin-left:6px;color:#444}

.newsletter{left:837px;top:359px;width:287px;height:325px;background:var(--panel)}
.newsletter-head{left:837px;top:367px;width:287px;height:103px;background:var(--bar-blue);border-top:1px dashed var(--white);border-bottom:1px dashed var(--white);outline:3px solid var(--bar-blue)}
.newsletter-head svg{position:absolute;left:28px;top:18px}
.newsletter-head .slogan{position:absolute;left:122px;top:20px;font-family:"Fjalla One",sans-serif;font-size:24px;line-height:28px;color:var(--white)}
.newsletter-copy{left:862px;top:492px;width:238px;text-align:center;font-size:13px;line-height:16px;color:var(--muted)}
.email-field{left:849px;top:581px;width:263px;height:30px;background:var(--white);border:1px solid #bbb;border-radius:6px;font-size:12px;color:var(--ink);padding:7px 0 0 13px}
.subscribe-btn{left:851px;top:623px;width:124px;height:38px;border-radius:5px;background:linear-gradient(#2ea3dc,#0a72b0);border:1px solid #0a65a0;color:var(--white);font-family:"Fjalla One",sans-serif;font-size:20px;display:flex;align-items:center;justify-content:center}

.share{left:837px;top:697px;width:287px;height:139px;background:var(--panel)}
.share-head{left:837px;top:707px;width:287px;height:51px;background:var(--bar-blue);border-top:1px dashed var(--white);border-bottom:1px dashed var(--white);display:flex;align-items:center;justify-content:center;font-family:"Fjalla One",sans-serif;font-size:27px;color:var(--white)}
.social{top:770px;width:50px;height:50px;background:#8a8a8a}

.site-footer{left:0;top:1082px;width:1143px;height:118px;background:var(--panel);text-align:center}
.site-footer .copyright{padding-top:28px;font-size:13.5px;color:var(--ink)}
.site-footer .credit{margin-top:8px;font-size:12px;color:#888}
</style>
</head>
<body>

<header class="abs site-header">
  <div class="abs brand-slot" role="img" aria-label="Retailer logo area"><span class="mark"></span><span class="name">website logo</span></div>
  <h1 class="abs page-title">Company Name Coupon Codes</h1>
</header>

<section class="abs welcome">
  <p>Welcome to the Company Name coupon page.</p>
  <p>Here you will find the best and most up to date coupon codes</p>
  <p>available directly from Company name</p>
</section>

<main>
  <div class="abs coupon-panel"></div>
  <h2 class="abs panel-bar">Featured Coupon Codaes</h2>

  <article class="abs coupon-card" style="top:428px">
    <h3 class="offer">$51.26 Average savings on Shopvale.com</h3>
    <p class="details">Receive up to 60% off + Extra 20% off Select Jewelry &amp; Watches.</p>
    <span class="code-label">Coupon Code:</span>
    <span class="code revealed">12FOR12</span>
    <span class="copy-hint"><b>Click</b> to copy code</span>
    <p class="expires">Offer Expires: Aug 24, 2013</p>
    <p class="store">Use this code when shopping at : <strong>Shopvale.com</strong></p>
  </article>

  <article class="abs coupon-card" style="top:580px">
    <h3 class="offer">Free Shipping</h3>
    <p class="details">Receive free shipping on orders over $50. The description<br>could wrap like this</p>
    <span class="code-label">Coupon Code:</span>
    <span class="code"></span>
    <p class="expires">Offer Expires: Aug 24, 2013</p>
    <p class="store">Use this code when shopping at : <strong>Shopvale.com</strong></p>
  </article>

  <article class="abs coupon-card" style="top:730px">
    <h3 class="offer">$51.26 Average savings on Shopvale.com</h3>
    <p class="details">Receive up to 60% off + Extra 20% off Select Jewelry &amp; Watches.</p>
    <span class="code-label">Coupon Code:</span>
    <span class="code"></span>
    <p class="expires">Offer Expires: Aug 24, 2013</p>
    <p class="store">Use this code when shopping at : <strong>Shopvale.com</strong></p>
  </article>

  <article class="abs coupon-card" style="top:883px">
    <h3 class="offer">Free Shipping</h3>
    <p class="details">Receive free shipping on orders over $50. The description<br>could wrap like this</p>
    <span class="code-label">Coupon Code:</span>
    <span class="code"></span>
    <p class="expires">Offer Expires: Aug 24, 2013</p>
    <p class="store">Use this code when shopping at : <strong>Shopvale.com</strong></p>
  </article>
</main>

<aside>
  <div class="abs newsletter"></div>
  <div class="abs newsletter-head">
    <svg width="68" height="58" viewBox="0 0 68 58" aria-hidden="true">
      <path d="M2 24 L34 2 L66 24 V56 H2 Z" fill="#fff"/>
      <rect x="14" y="12" width="40" height="26" fill="#0590d0"/>
      <rect x="22" y="19" width="24" height="3" fill="#fff"/>
      <rect x="22" y="25" width="24" height="3" fill="#fff"/>
      <path d="M2 24 L34 44 L66 24 V56 H2 Z" fill="#fff" stroke="#0590d0" stroke-width="2"/>
      <path d="M2 56 L26 38 M66 56 L42 38" stroke="#0590d0" stroke-width="2"/>
    </svg>
    <p class="slogan">Never Miss<br>Another Deal!</p>
  </div>
  <p class="abs newsletter-copy">Our coupons are updated frequently, so be sure to sign-up for our newsletter to receive notification of new coupon codes and exclusive offers.</p>
  <div class="abs email-field">Enter Your Email Address Here</div>
  <div class="abs subscribe-btn">subscribe</div>

  <div class="abs share"></div>
  <h2 class="abs share-head">share this site</h2>
  <span class="abs social" style="left:866px" role="img" aria-label="Share button"></span>
  <span class="abs social" style="left:925px" role="img" aria-label="Share button"></span>
  <span class="abs social" style="left:982px" role="img" aria-label="Share button"></span>
  <span class="abs social" style="left:1041px" role="img" aria-label="Share button"></span>
</aside>

<footer class="abs site-footer">
  <p class="copyright">Copyright © 2013 dealnook.com All rights reserved.</p>
  <p class="credit">This coupon site was created by PLW Deals</p>
</footer>

</body>
</html>
```